New, High-Tech Website for Venture Z - A Product Development Company

Venture Z is located in Silicon Valley, CA. We help companies build products from start to finish and everywhere in between. We build teams with top talent based on our customer's needs. We need a BRAND NEW website that looks innovative, fresh, new & modern. We want our website to impress companies that will hire us, as well as developers, designers, product people, etc.

The design is very important!

Target Market(s)

Small companies, entrepreneurs, anyone who needs help building a product or finding top talent

Industry/Entity Type

Tech

Coding

Coded - Design and coding required

Font styles to use
Sans Serif

Requirements
Must have
• Our logo (attached) and colors that look good with the logo.

**UPDATE - Site should be fully coded for WordPress and be MOBILE FRIENDLY. (Responsive Designs)
Nice to have
• We would love to see your ideas and if you have any other cool ideas to make our site POP and look attractive.

Please also let us know the following when you submit your design (in the notes section)!

1) Are we able to use any illustrations or images you provided legally? Would we need to pay any additional fees for images or illustrations?  If so, how much per picture/illustration?

2) If we choose your design, do your services include deploying the design to our Wordpress site?  Or, do you charge extra for this and how much?

3) If we choose your design, will this include any other page designs?  If so, how many?

4) If we choose your design, how much will you charge to design and implement other pages for us (like our contact us page, careers page, site map page, etc.) so our website looks cohesive?

5) What is your turnaround time for further page designs and implementations to the site?

6) Can you design AND implement surveys and/or custom questionnaires? What is the cost?
Should not have
• Nothing too "corporate" looking. For example, no images with men in suits around a large conference room because this doesn't represent who we are. We are more looking for images of people working - small startup company style.

Really cool, high tech illustrations are good too.

```html
<!DOCTYPE html>
<html lang="en">
<head>
<meta charset="utf-8">
<title>Venture Z – Product Development</title>
<link href="https://fonts.googleapis.com/css2?family=Michroma&family=Poppins:wght@400;500;600;700&display=swap" rel="stylesheet">
<style>
:root{
  --teal:#2ec0c6;
  --teal-dark:#1fa6ac;
  --navy:#2f3e5c;
  --ink:#2b2f3a;
  --muted:#4d5360;
  --pale:#eaf8fb;
  --line:#d9dde3;
  --peach:#f6c9b0;
  --white:#ffffff;
}
*{box-sizing:border-box;margin:0;padding:0}
html,body{width:1200px;height:4640px;overflow:hidden}
body{position:relative;background:var(--white);font-family:"Poppins",sans-serif;color:var(--ink)}
.abs{position:absolute}
.heading{font-family:"Michroma",sans-serif;font-size:23px;color:var(--ink);text-align:center;letter-spacing:.5px}
.heading-rule{width:92px;height:2px;background:var(--teal);margin:14px auto 0}
.pill{position:absolute;display:flex;align-items:center;justify-content:center;border-radius:30px;font-size:12px;font-weight:600;color:var(--white);text-decoration:none;white-space:nowrap}
.pill-dark{background:var(--navy)}
.pill-teal{background:var(--teal)}
.pill-ghost{border:1.5px solid var(--white);color:var(--white);font-weight:500}
.pill-white{background:var(--white);color:var(--navy)}
.ring-tail{position:absolute;width:34px;height:34px;border-radius:50%;border:3px solid var(--teal);background:var(--white)}

/* header */
.brand{left:162px;top:40px;display:flex;align-items:center;gap:12px}
.brand-dot{width:34px;height:34px;border-radius:50%;background:var(--teal)}
.brand-name{font-size:24px;font-weight:600;color:var(--navy)}
.nav-rule{left:450px;top:74px;width:590px;height:1px;background:var(--line)}
.nav a{position:absolute;top:99px;font-size:13px;color:var(--ink);text-decoration:none;transform:translateX(-50%);white-space:nowrap}
.nav a.active{color:var(--teal)}

/* hero */
.side-rule{left:76px;top:225px;width:1px;height:342px;background:var(--line)}
.side-social{left:62px;width:28px;height:28px;border-radius:50%;border:1.5px solid var(--teal);background:var(--white)}
.hero-title{left:162px;top:296px;font-size:30px;font-weight:700;color:var(--teal);letter-spacing:.5px}
.hero-sub{left:162px;top:336px;font-size:21px;line-height:31px;color:var(--ink)}
.hero-halo{left:560px;top:182px;width:430px;height:430px;border-radius:50%;background:var(--pale)}
.hero-art{left:520px;top:212px;width:520px;height:360px;border-radius:22px;
  background:linear-gradient(135deg,#2ec0c6 0%,#8fdde0 32%,#dff3f5 55%,#f6d6c3 78%,#f2b897 100%);
  box-shadow:0 14px 30px rgba(47,62,92,.14)}
.hero-base{left:515px;top:540px;width:535px;height:14px;border-radius:7px;background:var(--navy)}
.scroll-hint{left:588px;top:634px;width:22px;height:34px;border-radius:11px;border:1.5px solid var(--teal)}

/* welcome */
.welcome-photo{left:162px;top:708px;width:322px;height:322px;border-radius:50%;background:linear-gradient(135deg,#8f9a98,#c9cfcc 60%,#e6e9e8)}
.welcome-title{left:572px;top:722px;font-family:"Michroma",sans-serif;font-size:21px}
.welcome-lead{left:572px;top:776px;width:470px;font-size:14px;line-height:22px;color:var(--teal);font-weight:500}
.welcome-body{left:572px;top:829px;width:466px;font-size:13px;line-height:21.8px;color:var(--muted);letter-spacing:.3px}

/* audiences */
.audiences{left:0;top:1111px;width:1200px;height:828px;background:var(--pale)}
.card{position:absolute;width:266px;height:284px;background:var(--white);box-shadow:0 4px 14px rgba(47,62,92,.12)}
.card-img{margin:5px;height:155px}
.card p{padding:16px 20px 0;text-align:center;font-size:13px;line-height:21.5px;color:var(--muted)}
.card.active::after{content:"";position:absolute;left:0;right:0;bottom:0;height:3px;background:var(--teal)}

/* services */
.service-table{left:395px;top:2090px;width:410px;height:450px;border-radius:50%;
  background:radial-gradient(circle,#ffffff 0 24%,#2ec0c6 25% 33%,#ffffff 34% 40%,#e9f7f8 41% 62%,#f3f5f7 63% 100%)}
.service-core{left:540px;top:2250px;width:120px;height:120px;border-radius:50%;background:var(--white);display:flex;align-items:center;justify-content:center;font-family:"Michroma",sans-serif;font-size:13px;color:var(--navy)}
.service-ring{position:absolute;width:80px;height:80px;border-radius:50%;border:2px solid var(--teal);background:var(--white);display:flex;align-items:center;justify-content:center}
.service-ring span{width:30px;height:30px;border:2px solid #7b8494;border-radius:50%;position:relative}
.service-ring span::after{content:"";position:absolute;left:8px;top:8px;width:10px;height:10px;border-radius:50%;background:var(--teal)}
.service-label{position:absolute;font-size:17px;color:var(--ink);white-space:nowrap}

/* blog banner */
.blog-banner{left:0;top:2624px;width:1200px;height:292px;background:linear-gradient(100deg,#46536e,#5b6780 45%,#3e4b66)}
.blog-title{left:0;top:2716px;width:1200px;text-align:center;font-family:"Michroma",sans-serif;font-size:27px;color:var(--white)}

/* excite */
.excite-list li{position:absolute;left:162px;list-style:none;display:flex;align-items:center;gap:14px;font-size:15px;color:var(--ink)}
.excite-list i{width:22px;height:22px;border:1.6px solid #6d7584;border-radius:50%;display:block}
.framed{position:absolute;background:var(--white);padding:8px;box-shadow:0 4px 18px rgba(0,0,0,.15);border-radius:6px}
.framed div{width:100%;height:100%;border-radius:3px}

/* promise */
.promise{left:0;top:3447px;width:1200px;height:526px;background:var(--navy)}
.promise-list li{position:absolute;left:680px;list-style:none;display:flex;align-items:center;gap:11px;font-size:15px;color:var(--white)}
.promise-list i{width:14px;height:14px;border-radius:50%;background:var(--teal);display:block}

/* newsletter */
.newsletter-sub{left:0;top:4106px;width:1200px;text-align:center;font-size:14px;color:var(--ink)}
.field{position:absolute;top:4158px;width:187px;height:36px;border:1px solid var(--line);border-radius:20px;font-size:11px;color:#8a909b;padding:10px 18px}

/* footer */
.footer{left:0;top:4356px;width:1200px;height:284px;background:var(--navy)}
.footer-brand{left:162px;top:4440px;display:flex;align-items:center;gap:10px}
.footer-brand .brand-dot{width:28px;height:28px}
.footer-brand .brand-name{font-size:19px;color:var(--white)}
.social-item{position:absolute;left:923px;display:flex;align-items:center;gap:12px;font-size:14px;color:var(--white)}
.social-item i{width:28px;height:28px;border-radius:50%;border:1.5px solid var(--white);display:block}
.copyright{top:4602px;font-size:12px;color:var(--white)}
</style>
</head>
<body>

<header>
  <div class="abs brand"><span class="brand-dot"></span><span class="brand-name">Venture Z</span></div>
  <a class="pill pill-dark" style="left:603px;top:9px;width:211px;height:40px">Freelancers – Apply Now</a>
  <a class="pill pill-teal" style="left:830px;top:9px;width:210px;height:40px">Companies – Get In Touch</a>
  <div class="abs nav-rule"></div>
  <nav class="nav">
    <a class="active" style="left:469px">Home</a>
    <a style="left:565px">Services</a>
    <a style="left:662px">About</a>
    <a style="left:796px">Testimonials &amp; Press</a>
    <a style="left:934px">Careers</a>
    <a style="left:1023px">Blog</a>
  </nav>
</header>

<section>
  <div class="abs side-rule"></div>
  <span class="abs side-social" style="top:344px"></span>
  <span class="abs side-social" style="top:380px"></span>
  <span class="abs side-social" style="top:416px"></span>
  <h1 class="abs hero-title">WE HELP COMPANIES</h1>
  <p class="abs hero-sub">Build Products From Start To<br>Finish And Everywhere In Between</p>
  <a class="pill pill-teal" style="left:162px;top:416px;width:153px;height:36px">Contact Us Today</a>
  <div class="abs hero-halo"></div>
  <div class="abs hero-art" role="img" aria-label="Illustration of a team launching a product with a rocket, laptop, gears and a light bulb"></div>
  <div class="abs hero-base"></div>
  <div class="abs scroll-hint"></div>
</section>

<section>
  <div class="abs welcome-photo" role="img" aria-label="Photo of two colleagues working together at a laptop"></div>
  <h2 class="abs welcome-title">Welcome to Venture Z</h2>
  <p class="abs welcome-lead">Product-led, team-driven software development based in Silicon Valley, CA</p>
  <p class="abs welcome-body">We take a product-led, team-driven approach to software development, establishing the product mindset in early stage companies, and transforming to a product mindset in more mature companies. We are obsessed with building teams with the best people and then removing any obstacles preventing them from doing their best work.</p>
  <a class="pill pill-teal" style="left:572px;top:974px;width:112px;height:34px">Read More</a>
  <span class="ring-tail" style="left:676px;top:974px"></span>
</section>

<section class="abs audiences">
  <h2 class="heading" style="margin-top:77px">We Love To Work With</h2>
  <div class="heading-rule"></div>
  <div class="card" style="left:162px;top:145px"><div class="card-img" role="img" aria-label="Person lit by colourful code projections" style="background:linear-gradient(135deg,#1b2b6b,#7a3aa0 50%,#1d6fa8)"></div><p>Entrepreneurs with an idea who want to build a prototype</p></div>
  <div class="card active" style="left:466px;top:145px"><div class="card-img" role="img" aria-label="Top view of a startup team at a table" style="background:linear-gradient(135deg,#6f7a82,#a9b1b5 60%,#d0d4d2)"></div><p>Start Up companies who need a product built quickly and cost effectively</p></div>
  <div class="card" style="left:770px;top:145px"><div class="card-img" role="img" aria-label="Open-plan office with people at desks" style="background:linear-gradient(135deg,#9aa3a6,#dfe3e2 60%,#b8bfc0)"></div><p>Small or medium-sized, more established companies that want to ship great products faster, or simply ship</p></div>
  <div class="card" style="left:313px;top:459px"><div class="card-img" role="img" aria-label="Large audience at a conference" style="background:linear-gradient(135deg,#3b4d7a,#8a6f6a 55%,#bfb2a8)"></div><p>Larger sized companies that need Product consulting</p></div>
  <div class="card" style="left:617px;top:459px"><div class="card-img" role="img" aria-label="Empty modern office with desks" style="background:linear-gradient(135deg,#c8cdce,#eef0ef 55%,#9da5a7)"></div><p>Companies of all sizes that need great talent, quickly.</p></div>
</section>

<section>
  <h2 class="abs heading" style="left:0;top:2016px;width:1200px">Our Services</h2>
  <div class="abs service-table" role="img" aria-label="Illustration of a team seated around a round table, seen from above"></div>
  <div class="abs service-core">Venture Z</div>
  <div class="service-ring" style="left:306px;top:2149px"><span></span></div>
  <div class="service-ring" style="left:266px;top:2264px"><span></span></div>
  <div class="service-ring" style="left:306px;top:2377px"><span></span></div>
  <div class="service-ring" style="left:804px;top:2149px"><span></span></div>
  <div class="service-ring" style="left:844px;top:2264px"><span></span></div>
  <div class="service-ring" style="left:804px;top:2377px"><span></span></div>
  <span class="service-label" style="right:910px;top:2177px">Designers</span>
  <span class="service-label" style="right:950px;top:2292px">Developers</span>
  <span class="service-label" style="right:910px;top:2405px">QA</span>
  <span class="service-label" style="left:900px;top:2177px">Product Managers</span>
  <span class="service-label" style="left:940px;top:2292px">Researchers</span>
  <span class="service-label" style="left:900px;top:2405px">Engineers</span>
</section>

<section>
  <div class="abs blog-banner" role="img" aria-label="Desk with laptop, coffee cup and plant, under a navy overlay"></div>
  <h2 class="abs blog-title">Read Our Latest Blog Posts Here</h2>
  <a class="pill pill-teal" style="left:536px;top:2780px;width:102px;height:32px">Explore</a>
  <span class="ring-tail" style="left:626px;top:2779px"></span>
</section>

<section>
  <h2 class="abs heading" style="left:0;top:2994px;width:1200px">Things That Excite Us<div class="heading-rule"></div></h2>
  <ul class="excite-list">
    <li style="top:3076px"><i></i>Innovation</li>
    <li style="top:3120px"><i></i>Newdesign &amp; Technology</li>
    <li style="top:3164px"><i></i>Clear executive vision</li>
    <li style="top:3208px"><i></i>Customer feedback</li>
    <li style="top:3252px"><i></i>Bringing new ideas to life</li>
    <li style="top:3296px"><i></i>Adapting to change</li>
    <li style="top:3340px"><i></i>Happy Clients</li>
  </ul>
  <div class="framed" style="left:600px;top:3069px;width:437px;height:293px"><div role="img" aria-label="Person with arms raised on a mountain viewing platform above clouds" style="background:linear-gradient(180deg,#3f6fb3,#8fb0d6 45%,#e6ecf2 65%,#6f7680)"></div></div>
</section>

<section class="abs promise">
  <h2 class="heading" style="margin-top:81px;color:var(--white)">Things That We Promise</h2>
</section>
<div class="framed" style="left:162px;top:3596px;width:438px;height:297px"><div role="img" aria-label="Two fists bumping against a warm blurred background" style="background:linear-gradient(135deg,#b9ad8e,#e8dcc0 50%,#cfd3c8)"></div></div>
<ul class="promise-list">
  <li style="top:3619px"><i></i>Product Focused Work</li>
  <li style="top:3656px"><i></i>Experience, passion &amp; impact</li>
  <li style="top:3694px"><i></i>Focused strategies</li>
  <li style="top:3732px"><i></i>Great people &amp; high-performing teams</li>
  <li style="top:3770px"><i></i>Integrity, reliability &amp; security</li>
  <li style="top:3807px"><i></i>Data-driven &amp; design-centric results</li>
  <li style="top:3846px"><i></i>Top customer service for our clients</li>
</ul>

<section>
  <h2 class="abs heading" style="left:0;top:4052px;width:1200px">Unlock Wisdom</h2>
  <p class="abs newsletter-sub">Industry trends, tech updates, insights, thought leadership, success stories &amp; more...</p>
  <div class="field" style="left:326px">Name</div>
  <div class="field" style="left:527px">Email</div>
  <a class="pill pill-teal" style="left:729px;top:4158px;width:114px;height:36px">Get Access</a>
  <span class="ring-tail" style="left:834px;top:4159px"></span>
</section>

<svg class="abs" style="left:0;top:4262px" width="1200" height="100" viewBox="0 0 1200 100" aria-hidden="true">
  <path d="M0 70 C300 20 700 0 1200 30 L1200 100 L0 100 Z" fill="#bfe9ee"/>
  <path d="M0 88 C350 45 750 30 1200 55 L1200 100 L0 100 Z" fill="#5fcfd5"/>
  <path d="M0 100 C350 70 800 55 1200 80 L1200 100 Z" fill="#2f3e5c"/>
</svg>
<footer class="abs footer"></footer>
<div class="abs footer-brand"><span class="brand-dot"></span><span class="brand-name">Venture Z</span></div>
<a class="pill pill-teal" style="left:324px;top:4405px;width:103px;height:30px">Services</a>
<a class="pill pill-ghost" style="left:461px;top:4405px;width:101px;height:30px">Why Us</a>
<a class="pill pill-ghost" style="left:324px;top:4448px;width:103px;height:30px">Our Approach</a>
<a class="pill pill-ghost" style="left:461px;top:4448px;width:101px;height:30px">FAQs</a>
<a class="pill pill-white" style="left:621px;top:4405px;width:198px;height:34px">Freelancers – Apply Now</a>
<span class="ring-tail" style="left:814px;top:4405px;background:var(--navy)"></span>
<a class="pill pill-teal" style="left:621px;top:4459px;width:198px;height:34px">Companies – Get In Touch</a>
<span class="ring-tail" style="left:814px;top:4459px;background:var(--navy)"></span>
<div class="social-item" style="top:4401px"><i></i>Friendnet</div>
<div class="social-item" style="top:4441px"><i></i>Snapgram</div>
<div class="social-item" style="top:4482px"><i></i>Linkwork</div>
<p class="abs copyright" style="left:162px">Copyright © 2021 Venture Z. All Rights Reserved. Privacy Policy &nbsp;|&nbsp; Terms &amp; Conditions</p>
<p class="abs copyright" style="right:163px">Security &amp; Compliance</p>

</body>
</html>
```